Playing Card Design for Magician's Business Card

Hello! I am looking for a two-sided design for a business card.
The back of the card look like the back of a playing card and includes the following text:
Dorian Feldhaus
www.FeldWonders.com
BACK:
Please - focus most of your time and effort on the BACK DESIGN.
Make it look like a playing card.
I plan to use this design to print up custom playing cards that I use in my show and give away to guests.
No Bunnies No Top Hats!
Not for kids. This is for sophisticated sleight of hand performed for adults.
Mood: Slick, elegant + fun.
See the attached samples of cards I like.
FRONT:
Not much text required ... Please leave plenty of blank space - minimalist.
The front of the card will have
First Name
Website
Phone Number
Email Address
Target Market(s)
Event Planners
Targeting corporate special events and private parties.
Industry/Entity Type
Magician
Contact Information for Business Card
Dorian Feldhaus
Illusionist
www.FeldWonders.com
Colors
Designer to choose colors to be used in the design.
Requirements
Must have
- Back must look like a playing card back.
- BACK MUST INCLUDE the following text:
- Dorian Feldhaus
- www.FeldWonders.com
Nice to have
- Symmetrical Design for back so the card looks the same if upside down.
- Please see "All Seeing Eye" design attached. Remove the Latin phrase and replace with Dorian (top left) Feldhaus (top right)
- FeldWonders.com (Lower middle)
Should not have
- Bunny Rabbits
- Top Hats
- Kids ....

```html
<!DOCTYPE html>
<html lang="en">
<head>
<meta charset="utf-8">
<title>Dorian Feldhaus – Business Card</title>
<link rel="stylesheet" href="https://fonts.googleapis.com/css2?family=Rye&family=Cinzel:wght@400;500&display=swap">
<style>
  :root {
    --page: #e9e6e1;
    --paper-light: #fbfbfb;
    --paper-shade: #dedede;
    --ink: #3b4650;
    --ink-soft: #8a939b;
    --slate: #3c4751;
    --slate-deep: #313a43;
    --chalk: #f1f1f1;
    --chalk-soft: #d9dcdf;
  }
  * { box-sizing: border-box; margin: 0; padding: 0; }
  html, body { width: 1200px; height: 780px; overflow: hidden; }
  body { background: var(--page); position: relative; }

  .card {
    position: absolute;
    top: 100px;
    width: 330px;
    height: 580px;
    border-radius: 6px;
    overflow: hidden;
    box-shadow: 0 4px 14px rgba(0,0,0,.18);
  }

  /* ---------- Front ---------- */
  .card-front {
    left: 190px;
    background: radial-gradient(ellipse at 50% 45%, var(--paper-light) 0%, #f2f2f2 60%, var(--paper-shade) 100%);
    color: var(--ink);
  }
  .front-frame {
    position: absolute; inset: 22px;
    border: 1.5px solid var(--ink);
  }
  .corner-ornament {
    position: absolute; width: 78px; height: 60px;
    background: radial-gradient(ellipse at center, #9aa2a9 0%, #c8ccd0 70%, transparent 100%);
    border-radius: 40%;
  }
  .corner-ornament.tl { top: 12px; left: 12px; }
  .corner-ornament.tr { top: 12px; right: 12px; }
  .corner-ornament.bl { bottom: 12px; left: 12px; }
  .corner-ornament.br { bottom: 12px; right: 12px; }
  .front-emblem {
    position: absolute; left: 40px; top: 175px; width: 250px; height: 250px;
    border-radius: 50%;
    background: radial-gradient(circle, rgba(200,205,210,.35) 0%, rgba(200,205,210,.15) 70%, transparent 72%);
  }
  .front-content {
    position: absolute; left: 0; right: 0; top: 195px;
    text-align: center;
  }
  .front-name {
    font-family: 'Rye', serif;
    font-size: 22px; letter-spacing: 1px;
  }
  .front-role {
    display: flex; align-items: center; justify-content: center; gap: 8px;
    font-family: 'Cinzel', serif; font-size: 15px; letter-spacing: 2px;
    margin-top: 6px;
  }
  .front-role::before, .front-role::after {
    content: ""; width: 42px; height: 1.5px; background: var(--ink);
  }
  .front-contact {
    font-family: 'Cinzel', serif; font-size: 13px; line-height: 1.45;
    margin-top: 22px; letter-spacing: .5px;
  }
  .front-contact .phone { font-size: 15px; }
  .front-divider { display: block; margin: 16px auto 0; }

  /* ---------- Back ---------- */
  .card-back {
    left: 680px;
    background: radial-gradient(ellipse at 50% 50%, var(--slate) 0%, var(--slate-deep) 100%);
    color: var(--chalk);
  }
  .back-frame {
    position: absolute; inset: 16px;
    border: 1.5px solid var(--chalk-soft);
    border-radius: 4px;
  }
  .side-arc {
    position: absolute; top: 245px; width: 70px; height: 110px;
    border-radius: 50%; background: var(--chalk-soft);
  }
  .side-arc.left { left: -40px; }
  .side-arc.right { right: -40px; }
  .back-word {
    position: absolute; left: 0; right: 0;
    font-family: 'Rye', serif;
    text-align: center; color: var(--chalk);
    letter-spacing: 1px;
  }
  .back-first { top: 48px; font-size: 62px; }
  .back-last { top: 392px; font-size: 50px; }
  .back-rule { position: absolute; left: 40px; }
  .back-emblem {
    position: absolute; left: 85px; top: 175px; width: 160px; height: 180px;
    border-radius: 50%;
    background: radial-gradient(ellipse, #c9ced3 0%, #8e979f 45%, rgba(142,151,159,.25) 75%, transparent 78%);
  }
  .back-url {
    position: absolute; left: 40px; right: 40px; top: 478px;
    background: var(--chalk);
    color: var(--slate-deep);
    font-family: 'Cinzel', serif; font-weight: 500;
    font-size: 17px; text-align: center;
    padding: 6px 0;
  }
</style>
</head>
<body>

<section class="card card-front" aria-label="Business card front">
  <div class="front-frame"></div>
  <div class="corner-ornament tl" role="img" aria-label="Swirling corner ornament"></div>
  <div class="corner-ornament tr" role="img" aria-label="Swirling corner ornament"></div>
  <div class="corner-ornament bl" role="img" aria-label="Swirling corner ornament"></div>
  <div class="corner-ornament br" role="img" aria-label="Swirling corner ornament"></div>
  <div class="front-emblem" role="img" aria-label="Faint geometric circular pattern"></div>

  <div class="front-content">
    <h1 class="front-name">DORIAN FELDHAUS</h1>
    <p class="front-role">MAGICIAN</p>
    <div class="front-contact">
      <p class="phone">(555) 214 3870</p>
      <p>HELLO@FELDWONDERS.COM</p>
      <p>WWW.FELDWONDERS.COM</p>
    </div>
    <svg class="front-divider" width="230" height="14" viewBox="0 0 230 14" aria-hidden="true">
      <line x1="0" y1="7" x2="230" y2="7" stroke="#3b4650" stroke-width="1.2"/>
      <rect x="95" y="2" width="40" height="10" rx="5" fill="#8a939b"/>
    </svg>
  </div>
</section>

<section class="card card-back" aria-label="Business card back">
  <div class="back-frame"></div>
  <div class="side-arc left"></div>
  <div class="side-arc right"></div>

  <h2 class="back-word back-first">DORIAN</h2>

  <svg class="back-rule" style="top:150px" width="250" height="12" viewBox="0 0 250 12" aria-hidden="true">
    <line x1="0" y1="6" x2="250" y2="6" stroke="#d9dcdf" stroke-width="1.2"/>
    <rect x="119" y="0" width="12" height="12" transform="rotate(45 125 6)" fill="#d9dcdf"/>
  </svg>

  <div class="back-emblem" role="img" aria-label="Ornamental medallion framing a spade"></div>

  <svg class="back-rule" style="top:372px" width="250" height="12" viewBox="0 0 250 12" aria-hidden="true">
    <line x1="0" y1="6" x2="250" y2="6" stroke="#d9dcdf" stroke-width="1.2"/>
    <rect x="119" y="0" width="12" height="12" transform="rotate(45 125 6)" fill="#d9dcdf"/>
  </svg>

  <h2 class="back-word back-last">FELDHAUS</h2>
  <p class="back-url">www.FeldWonders.com</p>

  <svg class="back-rule" style="top:530px" width="250" height="12" viewBox="0 0 250 12" aria-hidden="true">
    <line x1="0" y1="6" x2="250" y2="6" stroke="#d9dcdf" stroke-width="1.2"/>
    <rect x="119" y="0" width="12" height="12" transform="rotate(45 125 6)" fill="#d9dcdf"/>
  </svg>
</section>

</body>
</html>
```